Wordpress Blog for Mobile Service Store

We need a website design for a genuine blog for related information to our mobile services we will provide in a future online shop (see a selection of products on our company page: http://www.corvexaplan.com/vas-catalogue/end-users.htm).

This blog is thought to engage our final clients to get in contact with us. We want to provide them useful information about our different product and give them various interaction possibilities, like feedback/comments, content rating, watch video/audio files, Social network Adding and subscriptions to our news feeds and Newsletter.

But at the same time, a way should be found that the blog doesn´t seem to be overloaded with information and that it will be very intuitive in use of all offered functionalities. A valuable extra would be developing of a design which is adaptable to future expansion and adaption of additional content, categories, boxes or adds of our products.
Updates

Hi everyone!

First of all, thanks a lot for taking part in our design project for our future Worldpress Blog Design for our mobile service store.

Up to now the Store looks like that (http://www.tundrashelfmart.com/es.html), but we thinking of major changes in design and a renaming of this store. It tooks us a time to define well the blog requirements, so it helps you a lot to check the short xcl., project brief and given examples beforehand to get a idea what we are looking for.

Based on the first submitted designs I want to give a short feedback:

• - The submitted designs up to now work with too dark/serious colors, please avoid black, where it isn´t necessary…visiting our blog should mean pleasure!
• Separate corporate & final clients design:
• The look and feel should be independent from our “Corvexa Plan” Company design, since we don’t want to make a direct reference to us within our new store. Our company itself, Corvexa Plan, has it’s own blog for their corporate news.
• - This blog is thought to connect with our end clients (someone like you and me) of our online store where we sell mobile apps (f.e. services for 1€ /month). So the design should be not that serious, but rather a touch more feminine and playful.
• - Not too many lists on main page! One section with reference to the most popular post is sufficient, a further reference to older post will be made at the bottom of a single post.
• - Out of our experience (more) pictures and visual elements catch more attention for a further reading  of a post (check out our given examples in the brief!), so we look for a more engaging post design, f.e. like the headlines of the new Quillstoat Blog.
• - Implement a sleek "advanced search bar", no need of a space-occupying "keyword cloud" - we want to avoid that our readers are overwhelmed with unnecessary  information.
So let´s get the best out of this!

We appreciate a lot your help!

Cheers, Henrike (marketing@corvexaplan.com)

Reason: Hi everyone, Since it´s holiday time here in Europe, might be that some of you are coming back from there right now...so we give you a week more time to submit your designs to our project. I will upload some more inside + pictures of our project to help to make it more easier for you what kind of design we are looking for. Thanks in advance for your dedication to our project =). Kind regards, Henrike =)

Target Market(s)

Our main target group are people who NOT owns a smart phone, but rather posses any kind of phone device, never mind how old, never mind the age, gender or profession.

By calling a land-line number everyone can have access to our Mobile Services. We offer services for professional use, but as well for leisure. Our clients have to pay for our service, so we want to transmit trust, proximity and professionalism.

The only criteria we have, is that our client has a minimum technical ability to subscribe himself to a service on our homepage and configure his account there.

Industry/Entity Type

Shop

Requirements
Must have
• Required design to the following screen- maximum width: 1400 px.
Design should be in a later stage adaptable to Worldpress Blog tool.
We need a design which visualize the main page and the single post.

!!! Please find attached an EXCEL FILE which lists all main components to implement in the design !!!

Look and feel (further inside)

Since we haven´t a final logo for our shop so far, neither a finished design we set any limits to your creativity (no restriction in color code). But in general we are looking for a modern, clean/tidy and fresh design which has an elegant, personable and playful touch.

We appreciate a lot innovative elements which distinguish from an ordinary blog design/structure. As it´s important that the site doesn´t appear too text heavy but rather has an engaging visual standout. Dynamic elements which open while making a mouse-over are, for example, nice features to cluster information so the page doesn´t seem to overloaded.

Concerning the content, find in this link in our existing company blog an example of news we used to publish: http://blog.corvexaplan.com/launch_tovidex. It´s important, that the font is not to small, but easy to read. That´s why a line spacing higher than 1.0 is wished for the blog post to meet this criteria.
Nice to have
• In the PDF Brief attached you find several URLs of Blogs which visualize in some part our main idea (please check them beforehand!)

Should not have
• We don´t look for an ordinary blog design.
Avoid too heavy text!

```html
<!DOCTYPE html>
<html lang="en">
<head>
<meta charset="utf-8">
<title>Corvexa Plan – Mobile Service Blog</title>
<link href="https://fonts.googleapis.com/css2?family=Arimo:ital,wght@0,400;0,700;1,700&family=Signika:wght@600;700&display=swap" rel="stylesheet">
<style>
:root{
  --ink:#1a1a1a;
  --text:#8a8a8a;
  --nav-dark:#111;
  --stage-bg:#ededed;
  --blue:#4cb8e2;
  --title-blue:#2aa3d6;
  --badge:#1f6f9c;
  --orange:#f48a1f;
  --purple:#8a5bb0;
  --green:#7bb52b;
  --red:#d6262a;
  --panel:#e3e3e3;
  --footer:#3a3b3d;
  --footer-text:#e8e8e8;
  --bottom:#161616;
}
*{box-sizing:border-box;margin:0;padding:0}
html,body{width:706px;height:1200px;overflow:hidden}
body{position:relative;background:#f1f1f1;font-family:"Arimo",Arial,sans-serif;color:var(--text)}
.abs{position:absolute}
.heading{font-family:"Signika",Arial,sans-serif;font-weight:700}

/* header */
.site-header{left:0;top:0;width:706px;height:76px;background:linear-gradient(#e6e6e6,#cfcfcf)}
.brand{left:38px;top:12px;display:flex;align-items:center;gap:8px}
.brand-dot{width:46px;height:46px;border-radius:50%;background:var(--ink)}
.brand-name{font-size:19px;color:var(--ink)}
.account{top:5px;display:flex;align-items:center;gap:6px;font-size:13px;color:var(--ink)}
.account i{display:block;width:17px;height:17px;background:var(--ink)}
.search{left:530px;top:34px;width:160px;height:22px;border-radius:11px;background:linear-gradient(#3a3a3a,#0c0c0c);font-size:9px;color:#aaa;padding:6px 0 0 26px}
.search b{position:absolute;right:3px;top:3px;width:16px;height:16px;border-radius:50%;background:#ddd;color:#222;font-size:7px;text-align:center;line-height:16px}

/* nav */
.main-nav{left:0;top:76px;width:706px;height:36px;background:linear-gradient(#3b3b3b,var(--nav-dark));display:flex;justify-content:center}
.main-nav a{font-family:"Signika",sans-serif;font-weight:700;font-size:12.5px;letter-spacing:.5px;color:#9a9a9a;text-decoration:none;padding:11px 18px 0;border-left:1px solid #555;height:36px}
.main-nav a:first-child{border:none;color:#fff}

/* slider */
.stage{left:0;top:112px;width:706px;height:244px;background:var(--stage-bg)}
.slider{left:55px;top:119px;width:596px;height:211px;border:4px solid #fff;box-shadow:0 14px 14px -8px rgba(0,0,0,.35);background:#2a2a2a}
.slide-art{left:200px;top:4px;width:290px;height:196px;background:radial-gradient(circle at 55% 40%,#5a5a5a,#2a2a2a 70%)}
.caption{left:2px;top:105px;width:222px;height:70px;background:rgba(20,20,20,.85);padding:6px 6px}
.caption .meta{font-size:7px;color:#ddd;font-style:italic;font-weight:700}
.caption .meta span{background:var(--red);color:#fff;padding:1px 3px;margin-right:3px}
.caption h2{font-family:"Arimo",sans-serif;font-size:11px;color:#fff;margin:8px 0 4px}
.caption p{font-size:7px;color:#eee;line-height:10px;padding-left:4px}
.caption p u{color:#6cc3ef}
.pager{left:519px;top:184px;width:60px;height:14px;background:#111;font-size:8px;color:#fff;display:flex;justify-content:center;gap:7px;line-height:14px}
.pager b{background:#fff;color:#000;padding:0 3px}
.arrow{top:216px;width:16px;height:16px;border-radius:50%;background:#111}

/* feature boxes */
.feature{top:362px;width:165px;height:116px;border-radius:8px;padding:4px 8px 0}
.feature h3{text-align:center;color:#fff;font-size:14px;margin-bottom:3px}
.feature .card{background:#fff;border-radius:5px;height:84px;font-size:7.3px;line-height:12.5px;font-weight:700;text-align:center;padding:5px 10px}
.video-note{width:60px;font-size:14px;line-height:14.5px;color:#777;text-align:center}
.login{left:530px;top:358px;width:160px;height:121px;background:var(--green);border:3px solid #fff;outline:1px solid #ccc;padding:6px 9px}
.login h3{color:#fff;font-size:13px}
.login .field{background:#fff;height:22px;margin-top:8px;font-size:9px;color:#888;padding:6px 8px}
.login .btn{margin:8px auto 0;width:38px;height:13px;border-radius:7px;background:#111;color:#fff;font-size:8.5px;text-align:center;font-weight:700}

/* posts */
.posts{left:17px;top:488px;width:499px;height:584px;background:var(--panel);border-radius:6px}
.author{left:6px;width:46px;font-size:8px;line-height:11px;color:#666;text-align:left}
.author .avatar{width:25px;height:25px;background:#fff;border:1px solid #bbb;margin:0 0 10px 2px}
.author .social{display:grid;grid-template-columns:14px 14px;gap:7px;margin:8px 0 0 4px}
.author .social i{width:14px;height:14px;background:#5e5e5e;display:block}
.post{left:58px;width:430px;background:#fff;box-shadow:0 1px 3px rgba(0,0,0,.2)}
.post-title{position:absolute;left:-14px;top:-3px;width:444px;height:20px;background:#bfe6f7;clip-path:polygon(14px 0,100% 0,100% 100%,14px 100%,0 50%);font-size:11px;color:var(--title-blue);padding:4px 0 0 20px}
.count{position:absolute;right:14px;top:1px;width:20px;height:12px;background:var(--badge);color:#fff;font-size:7px;text-align:center;line-height:12px}
.body{font-size:8.5px;line-height:16.5px;color:#999}
.lead{font-size:12px;line-height:16.5px;font-weight:700;color:#8a8a8a}
.ph{background:radial-gradient(circle,#9a9a9a,#e8e8e8 70%)}

/* sidebar */
.services-title{left:530px;top:486px;font-size:12px;font-weight:400;color:#333;width:160px;border-bottom:1px solid #bbb;padding-bottom:3px}
.service{left:530px;width:160px;font-size:8.3px;line-height:11.7px;color:#333;padding-left:20px;border-bottom:1px dotted #999;padding-bottom:5px}
.service i{position:absolute;left:2px;top:2px;width:11px;height:8px;background:#444}
.service .link{color:var(--title-blue)}
.service .time{color:#aaa}
.promo{left:528px;top:757px;width:162px;height:208px;background:linear-gradient(#fff,#eee);border-radius:6px;box-shadow:0 1px 3px rgba(0,0,0,.25)}
.promo .name{position:absolute;left:0;width:162px;top:33px;text-align:center;font-size:17px;color:var(--ink)}
.promo .mark{position:absolute;left:66px;top:8px;width:30px;height:24px;background:#333;border-radius:50%}
.promo p{position:absolute;left:9px;top:68px;width:148px;font-size:8.3px;line-height:11.7px;color:#999}
.promo .art{position:absolute;left:8px;top:122px;width:80px;height:84px;background:linear-gradient(#5cb3d6,#2b6f97)}
.promo .cta{position:absolute;left:76px;top:175px;width:82px;height:22px;background:var(--orange);color:#fff;font-size:10px;padding:5px 0 0 8px;clip-path:polygon(0 0,82% 0,100% 50%,82% 100%,0 100%)}
.newsletter{left:528px;top:972px;width:162px;height:52px;background:var(--green);border-radius:6px;border-bottom:4px solid #5e8f1d;padding:5px 4px}
.newsletter h4{text-align:center;color:#fff;font-size:8px;font-weight:700}
.newsletter .row{display:flex;gap:4px;margin-top:6px}
.newsletter .in{flex:1;background:#fff;height:15px;border-radius:3px;font-size:8px;padding:3px 5px;color:#888}
.newsletter .sub{background:#111;color:#fff;font-size:8.5px;font-weight:700;border-radius:6px;padding:2px 5px}

/* footer */
.footer{left:0;top:1080px;width:706px;height:92px;background:linear-gradient(#4a4b4d,var(--footer))}
.col{top:1089px;font-size:7.5px;line-height:10px;color:var(--footer-text)}
.col h5{font-size:7.5px;margin-bottom:7px;color:var(--footer-text)}
.footer-links{left:479px;top:1089px;font-size:7.5px;color:var(--footer-text);word-spacing:3px}
.circles{left:485px;top:1122px;display:flex;gap:7px}
.circles i{width:22px;height:22px;border-radius:50%;background:#dcdcdc;display:block}
.bottom{left:0;top:1172px;width:706px;height:28px;background:var(--bottom);font-size:7.5px;color:var(--footer-text);padding-top:10px}
</style>
</head>
<body>

<header class="abs site-header">
  <div class="abs brand"><span class="brand-dot"></span><span class="brand-name">Corvexa Plan</span></div>
  <div class="abs account" style="left:538px"><i></i>Log In</div>
  <div class="abs account" style="left:617px"><i></i>Register</div>
  <div class="abs search">Search<b>Go</b></div>
</header>

<nav class="abs main-nav"><a>Home</a><a>Store</a><a>Feedback</a><a>Contact</a></nav>

<section class="abs stage"></section>
<span class="abs arrow" style="left:27px"></span>
<span class="abs arrow" style="left:661px"></span>
<div class="abs slider">
  <div class="abs slide-art" role="img" aria-label="Tablet and phone showing app icons"></div>
  <div class="abs caption">
    <div class="meta"><span>/ NEWSFLASH 2 /</span>— Monday, February 15, 2010 12:42</div>
    <h2>Content of Newsflash 2</h2>
    <p>Sitecraft makes it easy to launch a Web site of any kind.<br>Whether you want a brochure site or you are... <u>Read more</u></p>
  </div>
  <div class="abs pager"><span>1</span><b>2</b><span>3</span></div>
</div>

<section class="abs feature" style="left:17px;background:var(--blue)">
  <h3 class="heading">Recent Posts</h3>
  <div class="card">The standard chunk of Lorem Ipsum used since the 1500s is reproduced below for inter-ested. Sections 1.10.32 and 1.10.33 from "de Finibus Bonorum et Malorum"</div>
</section>
<section class="abs feature" style="left:184px;background:var(--orange)">
  <h3 class="heading">Older Posts</h3>
  <div class="card">The standard chunk of Lorem Ipsum used since the 1500s is reproduced below for inter-ested. Sections 1.10.32 and 1.10.33 from "de Finibus Bonorum et Malorum"</div>
</section>
<section class="abs feature" style="left:350px;background:var(--purple)">
  <h3 class="heading">Clipcast Videos</h3>
  <div class="card" style="display:flex;gap:8px;padding:4px 6px">
    <div style="width:78px;height:62px;margin-top:6px;background:radial-gradient(circle,#777,#111 70%)" role="img" aria-label="Video thumbnail"></div>
    <div class="heading video-note">“Get more details from videos”</div>
  </div>
</section>
<section class="abs login">
  <h3 class="heading">Login</h3>
  <div class="field">username</div>
  <div class="field">password</div>
  <div class="btn">Login</div>
</section>

<main class="abs posts">
  <div class="abs author" style="top:12px"><div class="avatar"></div>Mel Jarrow<br>1 day ago<div class="social"><i></i><i></i><i></i><i></i></div></div>
  <article class="abs post" style="top:15px;height:101px">
    <h2 class="post-title heading">The standard chunk of Lorem Ipsum used since the 1500s<span class="count">6</span></h2>
    <p class="abs body" style="left:5px;top:24px;width:420px">The standard chunk of Lorem Ipsum used since the 1500s is reproduced below for those interested. Sections 1.10.32 and 1.10.33 from "de Finibus Bonorum et Malorum" by Varnus are also reproduced in their exact original form, accompanied by English versions from the 1914 translation by H. Dellow. It is &nbsp;the readable content of a page when looking at its layout.</p>
  </article>

  <div class="abs author" style="top:133px"><div class="avatar"></div>Mel Jarrow<br>1 day ago<div class="social"><i></i><i></i><i></i><i></i></div></div>
  <article class="abs post" style="top:136px;height:206px">
    <h2 class="post-title heading">The standard chunk of Lorem Ipsum used since the 1500s<span class="count">6</span></h2>
    <p class="abs lead" style="left:12px;top:34px;width:205px">The standard chunk of Lorem Ipsum used since the 1500s is re-produced below for those inter-</p>
    <div class="abs ph" style="left:14px;top:100px;width:180px;height:70px" role="img" aria-label="Smartphone lying on its side"></div>
    <p class="abs body" style="left:220px;top:32px;width:200px">The standard chunk of Lorem Ipsum used since the 1500s is reproduced below for those inter-ested. Sections 1.10.32 and 1.10.33 from "de Finibus Bonorum et Malorum" by Varnus are also reproduced in their exact original form, accom-panied by English versions from the 1914 trans-lation by H. Dellow.<br>It is &nbsp;the readable content of a page when look-ing at its layout.</p>
  </article>

  <div class="abs author" style="top:359px"><div class="avatar"></div>Mel Jarrow<br>1 day ago<div class="social"><i></i><i></i><i></i><i></i></div></div>
  <article class="abs post" style="top:362px;height:203px">
    <h2 class="post-title heading">The standard chunk of Lorem Ipsum used since the 1500s<span class="count">6</span></h2>
    <div class="abs ph" style="left:16px;top:40px;width:130px;height:150px" role="img" aria-label="App icons rising from a smartphone"></div>
    <p class="abs body" style="left:170px;top:30px;width:250px">The standard chunk of Lorem Ipsum used since the 1500s is reproduced below for those interested. Sections 1.10.32 and 1.10.33 from "de Finibus Bonorum et Malorum"</p>
    <p class="abs body" style="left:170px;top:84px;width:250px">Varnus are also reproduced in their exact original form, accompanied by English versions from the 1914 translation by H. Dellow.It is &nbsp;the readable content of a page when looking at its layout.</p>
    <p class="abs lead" style="left:170px;top:158px;width:255px">The standard chunk of Lorem Ipsum used since the 1500s is reproduced</p>
  </article>
</main>

<h3 class="abs services-title">Our Services</h3>
<div class="abs service" style="top:508px"><i></i>The standard chunk of Lorem Ipsum used since the 1500s is reproduced below for "de Finibus Bonorum et Malorum"<div class="link">Varnus are also reproduced</div><div class="time">18 hours, 25 mins ago</div></div>
<div class="abs service" style="top:591px"><i></i>The standard chunk of Lorem Ipsum used since the 1500s is reproduced below for "de Finibus Bonorum et Malorum"<div class="link">Varnus are also reproduced</div><div class="time">18 hours, 25 mints ago</div></div>
<div class="abs service" style="top:672px"><i></i>The standard chunk of Lorem Ipsum used since the 1500s is reproduced below for "de Finibus Bonorum et Malorum"<div class="link">Varnus are also reproduced</div><div class="time">18 hours, 25 mints ago</div></div>

<aside class="abs promo">
  <span class="mark"></span>
  <div class="name heading">MindCrate</div>
  <p>The standard chunk of Lorem Ipsum used since the 1500s is reproduced 1.10.32 and 1.10.33 from "de Finibus Bonorum et Malorum"</p>
  <div class="art" role="img" aria-label="Head silhouette filled with words"></div>
  <div class="cta">click here</div>
</aside>

<section class="abs newsletter">
  <h4>Subscribe for News letter</h4>
  <div class="row"><div class="in">Enter your mail ID</div><div class="sub">Submit</div></div>
</section>

<footer class="abs footer"></footer>
<div class="abs col" style="left:66px"><h5>Apps</h5>Business<br>Entertainment<br>Games<br>Navigation<br>Productivity<br>Social Networking</div>
<div class="abs col" style="left:159px"><h5>Apis</h5>Communication<br>Machine Learning<br>Maps &amp; Positioning<br>Media &amp; Graphics<br>NFC &amp; Sensor<br>Security</div>
<div class="abs col" style="left:256px"><h5>Developer Community</h5>Blog Posts<br>Forum Topics</div>
<div class="abs col" style="left:364px"><h5>About</h5>Newsletters<br>Commercial Use<br>Contact Us<br>Sitemap</div>
<div class="abs footer-links">Home &nbsp;| &nbsp;Store &nbsp;| &nbsp;Feedback &nbsp;| &nbsp;Contact Us</div>
<div class="abs circles"><i></i><i></i><i></i><i></i><i></i></div>
<div class="abs bottom"><span style="margin-left:172px">Copyright @ 2011 www.corvexaplan.com All rights reserved</span><span style="margin-left:28px">Terms and conditions &nbsp;| &nbsp;Privacy policy</span></div>

</body>
</html>
```